" A empresa foi criada para comercializar e prestar serviços especializados em softwares voltados para infraestrutura de tecnologia. Nosso ramo de atuação será a venda e entrega de soluções para clientes que possuem infraestrutura de tecnologia própria (on-premisses) e clientes que não possuem infraestrutura, utilizando nuvens públicas como TNQ e Morvek. "

```html
<!DOCTYPE html>
<html lang="pt-BR">
<head>
<meta charset="UTF-8">
<title>Crachá de identificação – Veltris</title>
<link rel="stylesheet" href="https://fonts.googleapis.com/css2?family=Montserrat:wght@400;600;700&display=swap">
<style>
  :root {
    --page-bg: #eceef0;
    --navy: #2a3566;
    --navy-deep: #222b58;
    --navy-soft: #34407a;
    --cyan: #27b4d8;
    --cyan-light: #8fd3ea;
    --white: #ffffff;
    --band: #f3f5f8;
    --grey-text: #5f6675;
  }
  * { margin: 0; padding: 0; box-sizing: border-box; }
  html, body {
    width: 1200px;
    height: 1200px;
    overflow: hidden;
    background: var(--page-bg);
    font-family: "Montserrat", sans-serif;
  }
  .canvas {
    width: 1200px;
    height: 1200px;
    display: flex;
    align-items: center;
    justify-content: center;
  }
  .badge {
    position: relative;
    width: 640px;
    height: 1000px;
    border-radius: 28px;
    background: var(--navy);
    overflow: hidden;
    box-shadow: 0 18px 40px rgba(30, 40, 80, 0.18);
  }
  .badge-pattern {
    position: absolute;
    inset: 0;
    width: 100%;
    height: 100%;
  }
  .clip-slot {
    position: absolute;
    top: 42px;
    left: 50%;
    transform: translateX(-50%);
    width: 150px;
    height: 26px;
    border-radius: 13px;
    background: var(--page-bg);
  }
  .brand {
    position: absolute;
    top: 150px;
    left: 0;
    right: 0;
    display: flex;
    justify-content: center;
    align-items: center;
    gap: 20px;
  }
  .brand-square {
    width: 64px;
    height: 64px;
    background: var(--cyan-light);
  }
  .brand-text { display: flex; flex-direction: column; }
  .brand-name {
    color: var(--white);
    font-weight: 600;
    font-size: 52px;
    letter-spacing: 3px;
    line-height: 1;
  }
  .brand-tagline {
    color: var(--cyan-light);
    font-weight: 600;
    font-size: 15px;
    letter-spacing: 2px;
    margin-top: 8px;
  }
  .photo-frame {
    position: absolute;
    top: 330px;
    left: 50%;
    transform: translateX(-50%);
    width: 250px;
    height: 290px;
    background: var(--white);
    padding: 12px;
  }
  .photo {
    width: 100%;
    height: 100%;
    background: linear-gradient(180deg, #c9cdd3 0%, #a9b0ba 55%, #3e4a6b 100%);
  }
  .name-band {
    position: absolute;
    top: 720px;
    left: 0;
    right: 0;
    height: 150px;
    background: var(--band);
    display: flex;
    flex-direction: column;
    align-items: center;
    justify-content: center;
    gap: 10px;
  }
  .holder-name {
    color: var(--cyan);
    font-size: 44px;
    font-weight: 400;
    letter-spacing: 1px;
  }
  .holder-role {
    color: var(--grey-text);
    font-size: 24px;
    font-weight: 400;
    letter-spacing: 1px;
  }
  .accent-strip {
    position: absolute;
    top: 890px;
    left: 0;
    right: 0;
    height: 14px;
    background: var(--cyan);
  }
</style>
</head>
<body>
<main class="canvas">
  <article class="badge">
    <svg class="badge-pattern" viewBox="0 0 640 1000" aria-hidden="true">
      <polygon points="0,0 260,0 0,420" fill="#2f3a6e"/>
      <polygon points="640,120 640,620 330,700" fill="#303c72"/>
      <polygon points="0,520 300,700 0,900" fill="#27316140"/>
      <polygon points="380,0 640,0 640,260" fill="#252f5e"/>
      <rect x="0" y="870" width="640" height="130" fill="#222b58"/>
    </svg>
    <div class="clip-slot"></div>
    <header class="brand">
      <span class="brand-square"></span>
      <div class="brand-text">
        <span class="brand-name">VELTRIS</span>
        <span class="brand-tagline">SOLUÇÕES EM TECNOLOGIA</span>
      </div>
    </header>
    <div class="photo-frame">
      <div class="photo" role="img" aria-label="Foto do colaborador"></div>
    </div>
    <section class="name-band">
      <p class="holder-name">NOME SOBRENOME</p>
      <p class="holder-role">CARGO/FUNÇÃO</p>
    </section>
    <div class="accent-strip"></div>
  </article>
</main>
</body>
</html>
```